Build a Website for www.Brightvantlots.net real estate website

i have an existing website [url removed, login to view] and it has been done in frontpage for years. i would like to update our website to be me friendly for updating information and content. i would like to have it look great and easy to search, input.

My scope would be an easy back of house to login and add new properties, prices and addresses and pictures and pdfs for people to download. the site would easily reorder properties by price, would need to (on the back of house) once we put in a property it would need a classification check box to have it appear on pages as to being: office, retail, industrial, vacant land, multi-family, Mobile Home/ RV Parks, Investment, Solds and Specialty as well as ability to create more classifications. will need about us page, Sales Page, Listings Page, Helpful Links and Partners Page, Buy/ Sell Contact us Page...

currently i have links on all my pictures that open the pdfs i have stored on our site. i would love to have an email capture or sign up that would ask people to sign up for periodic updates and new properties (popup when they go to listings); a search page would be great to allow them to search by category and also by price.

i envision a e-commerce site without the check out and pay but with a "cart of likes". more of a put properties they like in a cart and then at the end or by clicking on a property they can download a pdf or ask for more information

```html
<!DOCTYPE html>
<html lang="en">
<head>
<meta charset="utf-8">
<title>Larch &amp; Vey – Commercial Property Specialists</title>
<link href="https://fonts.googleapis.com/css2?family=Arimo:wght@400;700&display=swap" rel="stylesheet">
<style>
:root{
  --page:#141414;
  --band:#262626;
  --panel:#353535;
  --panel-dark:#1e1e1e;
  --nav-top:#5a5a5a;
  --nav-bottom:#2a2a2a;
  --text:#ffffff;
  --muted:#8a8a8a;
  --label:#6fa52c;
  --green:#7cc242;
  --lime:#a9c43b;
  --red:#d42a1c;
  --orange:#e7561c;
  --ink:#2b2b1a;
}
*{box-sizing:border-box;margin:0;padding:0}
html,body{width:870px;height:1200px;overflow:hidden}
body{background:var(--page);font-family:"Arimo",Arial,sans-serif;color:var(--text);position:relative}
.abs{position:absolute}

/* navigation */
.main-nav{left:50px;top:5px;width:770px;height:39px;border-radius:9px;
  background:linear-gradient(var(--nav-top),var(--nav-bottom));border:1px solid #6a6a6a;
  display:flex;align-items:center;justify-content:space-around;padding:0 40px 0 130px}
.main-nav a{color:#fff;font-size:10px;font-weight:700;text-decoration:none;padding:3px 12px;border-radius:9px}
.main-nav a.current{background:linear-gradient(#f4f4f4,#bdbdbd);color:#333}
.greeting{right:58px;top:48px;color:var(--green);font-size:11px;font-weight:700}

/* brand */
.brand{left:72px;top:46px;width:398px;height:82px;background:#f2f2f2;border:2px solid #999;
  display:flex;align-items:center;padding:0 12px 0 40px;gap:14px}
.brand-name{font-size:34px;font-weight:400;color:#222;letter-spacing:1px;line-height:1}
.brand-tag{font-size:10px;color:#444;letter-spacing:1px;margin-top:4px}
.brand-badge{width:78px;height:54px;background:#2a2a2a;margin-left:auto}

/* hero */
.hero-band{left:0;top:138px;width:870px;height:330px;background:var(--band)}
.featured{left:52px;top:141px;width:305px;height:313px;background:var(--panel-dark);border-radius:6px;padding-top:22px}
.featured-row{display:flex;align-items:center;height:85px;padding-left:58px;border-bottom:1px dotted #444;font-size:11px;color:var(--muted)}
.featured-row.active{background:#333;color:#fff;font-weight:700;border-bottom:none}
.thumb{width:75px;height:64px;border:2px solid #ddd;flex:none}
.featured-row ul{list-style:none;line-height:20px;margin-left:23px;width:77px}
.hero-photo{left:352px;top:136px;width:462px;height:326px;border:5px solid var(--orange);border-radius:8px;
  background:linear-gradient(#4f8fd8 0%,#9cc4ea 42%,#c98a3a 55%,#e3a436 68%,#4c7a2c 85%,#3a5e22 100%)}
.sale-badge{left:324px;top:378px;width:88px;height:88px;border-radius:50%;background:var(--orange);
  display:flex;align-items:center;justify-content:center;text-align:center;font-size:15px;font-style:italic;font-weight:700;line-height:16px;transform:rotate(-14deg)}

/* search */
.search{left:55px;top:500px;width:511px;height:235px;background:var(--panel);border-radius:7px;padding:22px 12px}
.search h2{font-size:25px;font-weight:400;margin-bottom:14px}
.search-row{display:flex;align-items:center;height:28px;font-size:9px;font-weight:700;color:var(--label)}
.field-label{width:73px}
.colon{width:22px;color:#fff}
.select{width:142px;height:16px;background:#fff;border:1px solid #888;color:#333;font-weight:400;font-size:8px;padding-left:4px;display:flex;align-items:center;position:relative}
.select::after{content:"";position:absolute;right:0;top:0;width:20px;height:14px;background:#666}
.text-input{height:16px;background:#fff;border:1px solid #888}
.radio{width:16px;height:16px;border-radius:50%;background:#fff;border:3px solid #9bb;margin-right:6px}
.radio.on{background:radial-gradient(#2c5d9a 35%,#fff 40%)}
.search-row .opt{color:#fff;font-weight:400;margin-right:16px}
.right-group{display:flex;align-items:center;margin-left:23px}
.right-group .field-label{width:65px}
.search-btn{margin-top:12px;width:58px;height:26px;border:none;background:var(--red);color:#fff;font-size:9px;font-weight:700;border-radius:3px;font-family:inherit}

/* why panel */
.why{left:579px;top:500px;width:230px;height:423px;background:var(--lime);border-radius:6px;padding:20px 16px;font-size:10px;color:var(--ink)}
.why p{line-height:15px}
.why .claim{color:var(--red);text-align:center;margin:8px 0 6px}
.agent{width:94px;height:110px;margin-left:1px;background:linear-gradient(#6a5a48,#b99f86 60%,#3b3b40)}
.agent.second{height:112px;background:linear-gradient(#d9d9d9,#c9a48b 55%,#fafafa)}
.why .pitch{margin-top:12px;text-align:justify;line-height:16px}

.phones{left:579px;top:948px;width:230px}
.phones h3{color:var(--red);font-size:14px;font-weight:400;line-height:14px;margin-bottom:10px}
.phones li{font-size:10px;font-weight:700;text-decoration:underline;line-height:21px;list-style:none;padding-left:12px;position:relative}
.phones li::before{content:"";position:absolute;left:2px;top:10px;width:3px;height:3px;background:#ccc}

/* property list */
.list-title{left:55px;top:757px;font-size:24px;font-weight:400}
.property-grid{left:55px;top:801px;display:grid;grid-template-columns:repeat(4,106px);column-gap:11px;row-gap:13px}
.property .photo{width:106px;height:78px;border:3px solid #eee;border-radius:3px}
.property dl{font-size:8px;font-weight:700;line-height:14px;margin-top:3px}
.property dd{color:var(--green)}
.p1{background:linear-gradient(#8fb8de,#b4a48a 50%,#5f7f3d)}
.p2{background:linear-gradient(#e0e4e6,#b9c0c4 60%,#8a9296)}
.p3{background:linear-gradient(#5e9ad6,#dcdcdc 55%,#4d7d35)}
.p4{background:linear-gradient(#7db0e4,#e9e9e9 50%,#7e8a82)}
.p5{background:linear-gradient(#6fa7de,#e0c38e 50%,#3fa9c9)}
.p6{background:linear-gradient(#7fb1e6,#6d8cb5 50%,#4b6b3b)}
.p7{background:linear-gradient(#78b0e6,#ececec 50%,#40b4d3)}
.p8{background:linear-gradient(#85b6e6,#a7866c 55%,#4f7a38)}

.footer-rule{left:0;top:1177px;width:870px;height:1px;background:#333}
</style>
</head>
<body>

<nav class="main-nav abs">
  <a class="current">Home</a><a>About Us</a><a>Listings</a><a>Buy/Sell</a><a>Referrals/Links</a><a>Contact</a><a>Login</a>
</nav>
<div class="greeting abs">Hi guest</div>

<header class="brand abs">
  <div>
    <div class="brand-name">Larch &amp; Vey</div>
    <div class="brand-tag">Commercial Property Specialists</div>
  </div>
  <div class="brand-badge"></div>
</header>

<div class="hero-band abs"></div>
<section class="featured abs">
  <div class="featured-row"><div class="thumb p8" role="img" aria-label="Photo of a two-storey villa"></div>
    <ul><li>Villa</li><li>2007 year</li><li>5000 sq.ft</li></ul><ul><li>Brick, glass</li><li>3 beds</li><li>2 baths</li></ul></div>
  <div class="featured-row"><div class="thumb p5" role="img" aria-label="Photo of a yellow villa"></div>
    <ul><li>Villa</li><li>2009 year</li><li>3500 sq.ft</li></ul><ul><li>Brick, glass</li><li>5 beds</li><li>3 baths</li></ul></div>
  <div class="featured-row active"><div class="thumb p3" role="img" aria-label="Photo of a villa with garden"></div>
    <ul><li>Villa</li><li>2010 year</li><li>4200 sq.ft</li></ul><ul><li>Brick, glass</li><li>4 beds</li><li>3 baths</li></ul></div>
</section>
<div class="hero-photo abs" role="img" aria-label="Large photo of a yellow single-storey house with brick chimney under blue sky"></div>
<div class="sale-badge abs">Home<br>for Sale</div>

<section class="search abs">
  <h2>Search Property</h2>
  <div class="search-row"><span class="field-label">I Want to</span><span class="colon">:</span>
    <span class="radio on"></span><span class="opt">Buy</span><span class="radio"></span><span class="opt">Rent</span></div>
  <div class="search-row"><span class="field-label">Category</span><span class="colon">:</span><span class="select">-- Select Category --</span>
    <span class="right-group"><span class="field-label">Sq. Area</span><span class="colon">:</span><span class="text-input" style="width:52px"></span><span class="colon" style="width:12px;text-align:center">-</span><span class="text-input" style="width:54px"></span><span style="color:#fff;font-weight:400;margin-left:3px">sq.feet</span></span></div>
  <div class="search-row"><span class="field-label">Location</span><span class="colon">:</span><span class="select">-- Select Location --</span>
    <span class="right-group"><span class="field-label">Budget</span><span class="colon">:</span><span class="text-input" style="width:52px"></span><span class="colon" style="width:12px;text-align:center">-</span><span class="text-input" style="width:54px"></span><span style="color:#fff;font-weight:400;margin-left:3px">$</span></span></div>
  <div class="search-row"><span class="field-label">Bedrooms</span><span class="colon">:</span><span class="text-input" style="width:142px"></span>
    <span class="right-group"><span class="field-label">Bathrooms</span><span class="colon">:</span><span class="text-input" style="width:142px"></span></span></div>
  <button class="search-btn">Search</button>
</section>

<aside class="why abs">
  <p>Why Should You Choose Larch &amp; Vey?</p>
  <p class="claim">Because WE MAKE Results</p>
  <div class="agent" role="img" aria-label="Portrait photo of the first partner"></div>
  <div class="agent second" role="img" aria-label="Portrait photo of the second partner"></div>
  <p class="pitch">Let Us SELL or LEASE Your Commercial Property Today... and you could be spending your profits tomorrow!</p>
</aside>

<section class="phones abs">
  <h3>IMPORTANT PHONE<br>NUMBERS</h3>
  <ul><li>TAMPA PHONE #'S</li><li>PINELLAS PHONE #'S</li><li>PASCO PHONE #'S</li></ul>
</section>

<h2 class="list-title abs">Property List</h2>
<section class="property-grid abs">
  <article class="property"><div class="photo p1" role="img" aria-label="Restaurant building photo"></div><dl><dt>Category : Restaurant</dt><dt>Location : Liverpool</dt><dt>Status : Rent</dt><dd>Price : 45000</dd></dl></article>
  <article class="property"><div class="photo p2" role="img" aria-label="Office interior photo"></div><dl><dt>Category : Office</dt><dt>Location : Manchester</dt><dt>Status : Buy</dt><dd>Price : 450000</dd></dl></article>
  <article class="property"><div class="photo p3" role="img" aria-label="Hotel building photo"></div><dl><dt>Category : Hotel</dt><dt>Location : Bristol</dt><dt>Status : Rent</dt><dd>Price : 15000</dd></dl></article>
  <article class="property"><div class="photo p4" role="img" aria-label="Modern house on vacant land photo"></div><dl><dt>Category : Vacant Land</dt><dt>Location : Wales</dt><dt>Status : Buy</dt><dd>Price : 540000</dd></dl></article>
  <article class="property"><div class="photo p5" role="img" aria-label="Villa with pool photo"></div><dl><dt>Category : Industrial</dt><dt>Location : Liverpool</dt><dt>Status : Rent</dt><dd>Price : 15000</dd></dl></article>
  <article class="property"><div class="photo p6" role="img" aria-label="Blue house photo"></div><dl><dt>Category : Vacant Land</dt><dt>Location : London</dt><dt>Status : Buy</dt><dd>Price : 255000</dd></dl></article>
  <article class="property"><div class="photo p7" role="img" aria-label="White house with pool photo"></div><dl><dt>Category : Industrial</dt><dt>Location : Manchester</dt><dt>Status : Rent</dt><dd>Price : 25000</dd></dl></article>
  <article class="property"><div class="photo p8" role="img" aria-label="Brick house photo"></div><dl><dt>Category : Business</dt><dt>Location : Wales</dt><dt>Status : Buy</dt><dd>Price : 540000</dd></dl></article>
</section>

<div class="footer-rule abs"></div>
</body>
</html>
```